TrueLane Collision Repair Web Site

Create a web site that will inform my potential customers about the services I provide. We are a Automotive Collision repair business that uses the latest state of the art equipment, computerized paint matching highly trained technicians, have over 30 years experience. We work with all all insurance programs. Our Moto is "Fixed Right, The First Time, Every Time". TrueLane, The intelligent choice in collision repair.

Target Market(s)

People that have been in a auto collision, needs windshield replaced, people that drive 10 year or newer cars

Industry/Entity Type

Automotive

Coding

Coded - Design and coding required

Number of Pages Required

4 page

Font styles to use
Sans Serif

Requirements
Must have
• Logo, Place for Phone number, I need to be able to put the code in so I can use a tracking phone number
• site needs to be mobile ready or adaptive
• May want to have a photo of a high end car
• here is a web site for example with the pages that I want
• https://www.brisvaleautobody.example/online-repair-estimate,
• https://www.brisvaleautobody.example/schedule-appointment
• https://www.brisvaleautobody.example/collision-repair/auto-body-repair
• https://www.brisvaleautobody.example/contact
Nice to have
• Be great if the Car in the log could have the front damaged then have it fix in a animation. Not sure if could be done here

```html
<!DOCTYPE html>
<html lang="en">
<head>
<meta charset="utf-8">
<title>TrueLane Collision Repair</title>
<link rel="stylesheet" href="https://fonts.googleapis.com/css2?family=Montserrat:wght@400;500;600;700;800&family=Lato:ital,wght@0,300;0,400;0,700;1,400&display=swap">
<style>
:root{
  --blue:#0b55a5;
  --blue-dark:#084a90;
  --green:#a3e02f;
  --green-dark:#8cc81f;
  --ink:#333;
  --muted:#666;
  --line:#d5d5d5;
  --bg:#f7f7f7;
  --footer:#333;
}
*{box-sizing:border-box;margin:0;padding:0}
html,body{width:1200px;height:2676px;overflow:hidden}
body{font-family:"Lato",sans-serif;color:var(--ink);background:#fff;position:relative}
a{color:inherit;text-decoration:none}

/* header */
.site-header{position:absolute;top:0;left:0;width:1200px;height:96px;background:#fff;box-shadow:0 2px 4px rgba(0,0,0,.12);z-index:2}
.brand{position:absolute;left:156px;top:28px;display:flex;align-items:center;gap:10px;font-family:"Montserrat",sans-serif;font-weight:700;font-size:30px;color:var(--blue)}
.brand-dot{width:16px;height:16px;border-radius:50%;background:var(--green)}
.util-nav{position:absolute;right:156px;top:26px;font-size:17px;color:#999;font-weight:300;display:flex;gap:12px;align-items:center}
.util-nav u{text-decoration:underline}
.main-nav{position:absolute;right:156px;top:69px;display:flex;gap:56px;font-family:"Montserrat",sans-serif;font-size:11px;font-weight:500;letter-spacing:1px;color:#222}
.main-nav .active{color:var(--green-dark)}

/* hero */
.hero{position:absolute;top:96px;left:0;width:1200px;height:480px;background:var(--bg)}
.hero-kicker{position:absolute;top:42px;width:1200px;text-align:center;font-family:"Montserrat",sans-serif;font-weight:700;font-size:20px;color:var(--blue);letter-spacing:.5px}
.hero-title{position:absolute;top:64px;width:1200px;text-align:center;font-family:"Montserrat",sans-serif;font-weight:800;font-size:58px;color:var(--blue);letter-spacing:1px}
.divider{position:absolute;left:208px;width:784px;height:1px;background:var(--line)}
.divider::after{content:"";position:absolute;left:384px;top:-1px;width:14px;height:14px;background:var(--bg);border-right:1px solid var(--line);border-bottom:1px solid var(--line);transform:rotate(45deg)}
.divider.white::after{background:#fff}
.hero-sub{position:absolute;top:184px;width:1200px;text-align:center;font-size:19px;color:#555;line-height:24px}

.service-strip{position:absolute;top:352px;left:156px;width:888px;height:224px;display:flex}
.service-tile{position:relative;flex:1;height:224px;color:#fff;text-align:center;font-family:"Montserrat",sans-serif}
.service-tile .name{position:absolute;top:90px;width:100%;font-size:20px;font-weight:500}
.service-tile .name small{display:block;font-size:14px;font-weight:500}
.t1{background:linear-gradient(135deg,#2a2f36,#5c6670 60%,#1c2026)}
.t2{background:linear-gradient(135deg,#6e7c88,#a0aab2 50%,#7a4d48)}
.t3{background:linear-gradient(135deg,#3c4148,#70777e 50%,#2c3036)}
.t4{background:linear-gradient(135deg,#c9ccd0,#8c9aa6 50%,#55606b)}
.t5{background:linear-gradient(135deg,#3d4247,#6f757a 50%,#22262a)}
.t2 .name{top:56px}
.find-more{position:absolute;bottom:0;left:0;width:100%;height:34px;background:var(--green);color:#234;font-size:9px;font-weight:600;letter-spacing:1px;line-height:34px}
.tile-arrow{position:absolute;top:140px;left:80px;width:16px;height:2px;background:var(--green)}
.arrow-btn{position:absolute;width:28px;height:28px;border:1px solid var(--blue);background:#fff;display:flex;align-items:center;justify-content:center}
.arrow-btn.fill{background:var(--blue)}

/* process */
.process{position:absolute;top:576px;left:0;width:1200px;height:552px;background:#fff}
.section-title{position:absolute;width:1200px;text-align:center;font-family:"Montserrat",sans-serif;font-weight:700;font-size:29px;color:var(--blue)}
.process-intro{position:absolute;top:76px;left:230px;width:740px;text-align:center;font-size:14px;color:#555;line-height:18px}
.steps{position:absolute;top:172px;left:208px;width:784px;display:flex;justify-content:space-between}
.step{width:152px;height:152px;border-radius:50%;border:1px solid var(--blue);overflow:hidden;position:relative;background:#fff}
.step::after{content:"";position:absolute;left:0;bottom:0;width:100%;height:64px;background:var(--blue)}
.step .label{position:absolute;bottom:36px;width:100%;text-align:center;font-family:"Montserrat",sans-serif;font-size:12px;font-weight:500;color:#fff;z-index:1}
.step svg{position:absolute;left:50%;top:50px;transform:translateX(-50%);z-index:1}
.step.current{border:none;box-shadow:0 4px 8px rgba(0,0,0,.2);background:var(--blue)}
.step.current::after{background:#fff}
.step.current .label{color:var(--blue)}
.step-detail{position:absolute;top:352px;left:231px;width:720px}
.step-detail h3{font-family:"Montserrat",sans-serif;font-weight:500;font-size:20px;color:#222;margin-bottom:14px}
.step-detail p{font-size:13.5px;color:#666;line-height:18px;font-weight:300}
.learn-more{position:absolute;top:486px;left:231px;font-size:13px;font-style:italic;color:var(--green-dark);border-bottom:1px solid var(--green-dark)}

/* features */
.features{position:absolute;top:1128px;left:0;width:1200px;height:491px;background:linear-gradient(100deg,#eaeaea,#f6f6f6 50%,#eeeeee)}
.features-photo{position:absolute;left:0;top:0;width:460px;height:491px;background:linear-gradient(135deg,#b98f73,#4a5f86 55%,#1d2f63)}
.feature-list{position:absolute;left:156px;top:32px;width:304px;list-style:none}
.feature-list li{height:54px;background:var(--green);border-bottom:1px solid #7fb21c;display:flex;align-items:center;font-family:"Montserrat",sans-serif;font-size:14.5px;font-weight:500;color:#222;position:relative}
.feature-list li .ic{width:78px;height:100%;display:flex;align-items:center;justify-content:center;border-right:1px solid #8cc81f}
.feature-list li .tx{padding-left:14px}
.feature-list li.active{background:#2a2a2a;color:#fff}
.feature-list li.active::after{content:"";position:absolute;right:-12px;top:15px;border-left:12px solid #2a2a2a;border-top:12px solid transparent;border-bottom:12px solid transparent}
.warranty{position:absolute;left:540px;top:56px;width:500px;text-align:center}
.warranty h3{font-family:"Montserrat",sans-serif;font-weight:600;font-size:24px;color:#222;margin-bottom:16px}
.warranty p{font-size:13.5px;color:#555;line-height:17.6px;font-weight:300}
.warranty .read{display:inline-block;margin-top:36px;font-size:13.5px;font-style:italic;color:#333;border-bottom:1px solid #333}
.contact-box{position:absolute;left:610px;top:346px;width:360px;border-top:1px solid #ddd;text-align:center;padding-top:26px}
.contact-box h4{font-family:"Montserrat",sans-serif;font-weight:600;font-size:19px;color:#222}
.contact-box .num{font-family:"Montserrat",sans-serif;font-size:29px;color:#222;margin-top:4px}

/* reviews */
.reviews{position:absolute;top:1619px;left:0;width:1200px;height:521px;background:#fff}
.review-card{position:absolute;top:140px;left:208px;width:356px;height:332px;background:linear-gradient(135deg,#3d4b50,#26353a 60%,#1a2427);color:#fff}
.quote-mark{font-family:"Montserrat",sans-serif;font-size:40px;font-weight:800;color:var(--green);line-height:1;position:absolute;left:24px;top:18px}
.review-text{position:absolute;left:52px;top:50px;width:250px;font-size:13.5px;line-height:17.6px;font-weight:300}
.reviewer{position:absolute;left:52px;top:222px;font-family:"Montserrat",sans-serif;font-size:19px;font-weight:500}
.reviewer-loc{position:absolute;left:52px;top:248px;font-size:11.5px;line-height:17px;width:150px}
.review-submit{position:absolute;bottom:0;left:0;width:100%;height:34px;background:var(--green);text-align:center;line-height:34px;font-family:"Montserrat",sans-serif;font-size:9.5px;font-weight:600;letter-spacing:1px;color:#234}
.review-plain{position:absolute;top:140px;left:636px;width:356px;height:332px;border-bottom:4px solid var(--green)}
.review-plain .review-text,.review-plain .reviewer-loc{color:#666}
.review-plain .reviewer{color:#222}

/* offers */
.offers{position:absolute;top:2140px;left:0;width:1200px;height:232px;background:var(--bg)}
.offers svg.band{position:absolute;left:0;top:0}
.offers-copy{position:absolute;left:156px;top:34px;width:400px;color:#fff}
.offers-copy h3{font-family:"Montserrat",sans-serif;font-weight:700;font-size:24px;margin-bottom:12px}
.offers-copy p{font-size:13.5px;line-height:17.6px}
.btn-green{display:inline-block;margin-top:32px;height:33px;line-height:33px;padding:0 18px;background:var(--green);color:#234;font-family:"Montserrat",sans-serif;font-size:10px;font-weight:600;letter-spacing:1px}
.locator{position:absolute;left:688px;top:34px;width:356px}
.locator h3{font-family:"Montserrat",sans-serif;font-weight:700;font-size:24px;color:var(--blue);margin-bottom:14px}
.search{height:36px;border:1px solid #ccc;background:#fff;display:flex;align-items:center;padding:0 12px;gap:10px;font-size:13.5px;color:#999;font-weight:300}
.search span{flex:1}
.locator p{margin-top:28px;font-size:13.5px}
.locator .num{font-family:"Montserrat",sans-serif;font-size:23px;margin-top:2px}

/* footer */
.site-footer{position:absolute;top:2372px;left:0;width:1200px;height:304px;background:var(--footer);color:#ddd}
.f-about{position:absolute;left:156px;top:44px;width:300px}
.f-about h4{font-family:"Montserrat",sans-serif;font-size:19px;font-weight:400;color:#fff}
.f-about h4 b{font-weight:700}
.f-about p{font-size:13.5px;line-height:17.6px;margin-top:22px;color:#ccc}
.f-about .social-label{margin-top:18px;font-size:13.5px}
.social{display:flex;gap:6px;margin-top:12px}
.social i{width:24px;height:24px;background:#666;display:block}
.social i.on{background:var(--green)}
.f-copy{margin-top:34px;font-size:11.5px;line-height:15px;color:#bbb}
.f-links{position:absolute;left:512px;top:44px}
.f-links h4,.f-loc h4{font-family:"Montserrat",sans-serif;font-size:16px;font-weight:500;color:#fff;margin-bottom:18px}
.f-cols{display:flex;gap:50px}
.f-cols ul{list-style:none;font-size:12px;line-height:19px;font-family:"Montserrat",sans-serif;color:#ccc}
.f-cols li::before{content:"•";margin-right:10px;color:#999}
.f-cols li.on{color:var(--green)}
.f-loc{position:absolute;left:840px;top:44px;font-family:"Montserrat",sans-serif;font-size:13px;line-height:17.6px;color:#ddd}
.f-loc p{margin-bottom:18px}
.to-top{position:absolute;left:1092px;top:56px}
</style>
</head>
<body>

<header class="site-header">
  <a class="brand" href="#"><span class="brand-dot"></span>TrueLane</a>
  <div class="util-nav">
    <svg width="10" height="14" viewBox="0 0 10 14"><path d="M5 0a5 5 0 0 0-5 5c0 4 5 9 5 9s5-5 5-9a5 5 0 0 0-5-5zm0 7a2 2 0 1 1 0-4 2 2 0 0 1 0 4z" fill="#999"/></svg>
    <u>Locations</u> <span>/</span>
    <svg width="6" height="14" viewBox="0 0 6 14"><circle cx="3" cy="2" r="2" fill="#999"/><rect x="1" y="5" width="4" height="9" fill="#999"/></svg>
    <span>Repair Status</span> <span>/</span>
    <svg width="8" height="13" viewBox="0 0 8 13"><rect x="0.5" y="0.5" width="7" height="12" rx="1" fill="none" stroke="#999"/></svg>
    <span>(123) 456 7890</span>
  </div>
  <nav class="main-nav">
    <a class="active" href="#">— COMPANY —</a>
    <a href="#">REPAIR SERVICES</a>
    <a href="#">OUR PROCESS</a>
    <a href="#">CAREERS</a>
    <a href="#">CONTACT</a>
  </nav>
</header>

<section class="hero">
  <div class="hero-kicker">AUTO BODY &nbsp;/&nbsp; COLLISION &nbsp;/&nbsp; WINDSHIELD</div>
  <h1 class="hero-title">REPAIR</h1>
  <div class="divider" style="top:143px"></div>
  <p class="hero-sub">TrueLane Specialists in Collision<br>Auto Body Repair</p>
</section>

<div class="service-strip">
  <div class="service-tile t1" role="img" aria-label="Technician removing a dent from a car body"><div class="name">Auto Dent<small>Removal</small></div></div>
  <div class="service-tile t2" role="img" aria-label="Technician performing paintless dent repair on a red car"><div class="name">Paintless Dent<small>Repair</small></div><span class="tile-arrow"></span><div class="find-more">— FIND OUT MORE —</div></div>
  <div class="service-tile t3" role="img" aria-label="Close-up of a cracked windshield"><div class="name">Windshield<small>Repairs</small></div></div>
  <div class="service-tile t4" role="img" aria-label="Car bumper being repaired"><div class="name">Bumper<small>Repair</small></div></div>
  <div class="service-tile t5" role="img" aria-label="Hands working on a car fender"><div class="name">Fender<small>Repair</small></div></div>
</div>
<span class="arrow-btn" style="left:142px;top:450px"><svg width="8" height="12"><path d="M6 1 1 6l5 5" stroke="#0b55a5" stroke-width="2" fill="none"/></svg></span>
<span class="arrow-btn fill" style="left:1030px;top:450px"><svg width="8" height="12"><path d="m2 1 5 5-5 5" stroke="#fff" stroke-width="2" fill="none"/></svg></span>

<section class="process">
  <h2 class="section-title" style="top:40px">Repair Process</h2>
  <p class="process-intro">The TrueLane seven-step repair process ensures your vehicle is inspected and repaired only by industry-certified technicians, whose priority is getting you back on the road safely.</p>
  <div class="divider white" style="top:131px"></div>
  <span class="arrow-btn" style="left:142px;top:251px"><svg width="8" height="12"><path d="M6 1 1 6l5 5" stroke="#0b55a5" stroke-width="2" fill="none"/></svg></span>
  <span class="arrow-btn" style="left:1030px;top:251px"><svg width="8" height="12"><path d="m2 1 5 5-5 5" stroke="#0b55a5" stroke-width="2" fill="none"/></svg></span>
  <div class="steps">
    <div class="step"><svg width="44" height="40" viewBox="0 0 44 40"><rect x="2" y="2" width="40" height="36" fill="none" stroke="#0b55a5" stroke-width="2"/><path d="M2 7h40M2 11h40" stroke="#0b55a5"/><rect x="10" y="22" width="24" height="12" rx="3" fill="#0b55a5"/><path d="M13 22l3-6h12l3 6" fill="#0b55a5"/></svg><span class="label">Vehicle Drop Off</span></div>
    <div class="step current"><svg width="56" height="34" viewBox="0 0 56 34"><path d="M4 16l8-8h24l10 8h6v8H4z" fill="#fff"/><circle cx="14" cy="24" r="4" fill="#0b55a5" stroke="#fff" stroke-width="2"/><circle cx="42" cy="24" r="4" fill="#0b55a5" stroke="#fff" stroke-width="2"/><rect x="24" y="26" width="8" height="8" fill="#fff"/></svg><span class="label">Body Repair</span></div>
    <div class="step"><svg width="40" height="46" viewBox="0 0 40 46"><rect x="20" y="0" width="6" height="14" fill="#0b55a5"/><path d="M16 14h14l-2 16h-10z" fill="#0b55a5"/><rect x="24" y="28" width="5" height="16" fill="#0b55a5"/><path d="M2 24l12 0M4 30l10-2M2 34l12-4" stroke="#0b55a5" stroke-dasharray="2 2"/></svg><span class="label">Painting / Polish</span></div>
    <div class="step"><svg width="44" height="44" viewBox="0 0 44 44"><circle cx="22" cy="22" r="20" fill="#0b55a5"/><circle cx="22" cy="22" r="13" fill="none" stroke="#fff" stroke-width="3"/><circle cx="22" cy="22" r="4" fill="#fff"/><path d="M22 9v9M22 26v9M9 22h9M26 22h9" stroke="#fff" stroke-width="3"/></svg><span class="label">Reassembly</span></div>
  </div>
  <div class="step-detail">
    <h3>Body Repair</h3>
    <p>After your vehicle is evaluated, it moves into the body shop, where we remove all parts requiring separate repair or replacement, and perform body and structural repair work. Meanwhile, all repair work undergoes a rigorous quality control inspection.</p>
  </div>
  <a class="learn-more" href="#">Learn More »</a>
</section>

<section class="features">
  <div class="features-photo" role="img" aria-label="Smiling mechanic working on a car engine"></div>
  <ul class="feature-list">
    <li><span class="ic"><svg width="32" height="22"><rect x="2" y="8" width="20" height="10" rx="2" fill="none" stroke="#fff" stroke-width="2"/><circle cx="24" cy="10" r="6" fill="none" stroke="#fff" stroke-width="2"/><path d="M28 14l3 3" stroke="#fff" stroke-width="2"/></svg></span><span class="tx">All Makes &amp; Models</span></li>
    <li class="active"><span class="ic"><svg width="26" height="26"><circle cx="13" cy="11" r="9" fill="none" stroke="#fff" stroke-width="2"/><path d="M9 11l3 3 5-6" stroke="#fff" stroke-width="2" fill="none"/><path d="M7 19l-3 6h18l-3-6" stroke="#fff" stroke-width="2" fill="none"/></svg></span><span class="tx">Lifetime Warranty</span></li>
    <li><span class="ic"><svg width="22" height="24"><path d="M11 1l9 4v7c0 6-4 10-9 11-5-1-9-5-9-11V5z" fill="#fff"/><path d="M7 12l3 3 5-6" stroke="#8cc81f" stroke-width="2" fill="none"/></svg></span><span class="tx">Quality Control</span></li>
    <li><span class="ic"><svg width="20" height="26"><rect x="1" y="1" width="18" height="24" fill="none" stroke="#fff" stroke-width="2"/><rect x="4" y="4" width="12" height="5" fill="#fff"/><path d="M5 13h2M9 13h2M13 13h2M5 17h2M9 17h2M13 17h2M5 21h2M9 21h2M13 21h2" stroke="#fff" stroke-width="2"/></svg></span><span class="tx">Free Estimates</span></li>
    <li><span class="ic"><svg width="36" height="24"><path d="M2 14l4-8h16l4 8v6H2z" fill="none" stroke="#fff" stroke-width="2"/><circle cx="27" cy="15" r="7" fill="none" stroke="#fff" stroke-width="2"/><path d="M27 11v4h3" stroke="#fff" stroke-width="2" fill="none"/></svg></span><span class="tx">Car Rentals &amp; Towing</span></li>
    <li><span class="ic"><svg width="26" height="26"><circle cx="13" cy="13" r="8" fill="none" stroke="#fff" stroke-width="4" stroke-dasharray="4 3"/><circle cx="13" cy="13" r="3" fill="#fff"/></svg></span><span class="tx">Insurance Partners</span></li>
    <li><span class="ic"><svg width="32" height="22"><rect x="1" y="1" width="30" height="20" fill="none" stroke="#fff" stroke-width="2"/><circle cx="16" cy="10" r="4" fill="none" stroke="#fff" stroke-width="2"/></svg></span><span class="tx">Dealer Certified</span></li>
    <li><span class="ic"><svg width="34" height="22"><rect x="1" y="2" width="26" height="17" rx="2" fill="none" stroke="#fff" stroke-width="2"/><rect x="1" y="6" width="26" height="3" fill="#fff"/><circle cx="27" cy="15" r="5" fill="#8cc81f" stroke="#fff" stroke-width="2"/></svg></span><span class="tx">Payment Options</span></li>
  </ul>
  <div class="warranty">
    <h3>Lifetime Warranty</h3>
    <p>At TrueLane, we proudly stand by the quality of our work.<br>That's why every repair performed at each of our locations nationwide is backed<br>by the TrueLane lifetime warranty. In the rare instance that<br>you're not 100 percent satisfied with the quality of your repair, simply<br>return your vehicle to any location and our team will work to make<br>it right. Guaranteed.</p>
    <a class="read" href="#">Read More »</a>
  </div>
  <div class="contact-box">
    <h4>Contact Us</h4>
    <div class="num">123.456.7890</div>
  </div>
</section>

<section class="reviews">
  <h2 class="section-title" style="top:38px">What Our Customer Says?</h2>
  <div class="divider white" style="top:93px"></div>
  <span class="arrow-btn" style="left:142px;top:292px"><svg width="8" height="12"><path d="M6 1 1 6l5 5" stroke="#0b55a5" stroke-width="2" fill="none"/></svg></span>
  <span class="arrow-btn" style="left:1030px;top:292px"><svg width="8" height="12"><path d="m2 1 5 5-5 5" stroke="#0b55a5" stroke-width="2" fill="none"/></svg></span>
  <div class="review-card" role="img" aria-label="Portrait of a customer in a suit, darkened behind the review">
    <span class="quote-mark">“</span>
    <p class="review-text">Outstanding customer focus &amp; service Greeted professionally by Sam and Admin Guided me thru the process all the way thru Kept in constant communication (text, phone) on repair status Promised and delivered on job completion Excellent pick-up and discharge/ paperwork process ...</p>
    <div class="reviewer">Daniel R</div>
    <div class="reviewer-loc">FL - 2210 Harbor View Rd, Eastmoor.</div>
    <div class="review-submit">— SUBMIT YOUR REVIEWS —</div>
  </div>
  <div class="review-plain">
    <span class="quote-mark">“</span>
    <p class="review-text">WOW! This is the first time that I have used Brisvale. I highly "wreck-ommend" this facility to anyone who lives in the Ridgeport, In area. The staff's first priority is to their customer! Pleasant, professional, respectful and diligent are a few adjectives that I'd use to describe the service that I received ...</p>
    <div class="reviewer">Laura K</div>
    <div class="reviewer-loc">FL - 740 W Maple Crest Ave, Pinehollow</div>
  </div>
</section>

<section class="offers">
  <svg class="band" width="1200" height="232" viewBox="0 0 1200 232"><polygon points="0,0 664,0 536,232 0,232" fill="#0b55a5"/></svg>
  <div class="offers-copy">
    <h3>Brisvale Offers!</h3>
    <p>Valuable savings and special offers on our repair services.<br>Take advantage of these offers exclusively available at Brisvale Collision &amp; Glass.</p>
    <a class="btn-green" href="#">— VIEW OFFERS —</a>
  </div>
  <div class="locator">
    <h3>Find a Center Near You</h3>
    <div class="search">
      <svg width="14" height="14"><circle cx="7" cy="7" r="5" fill="none" stroke="#bbb"/><circle cx="7" cy="7" r="2" fill="#bbb"/></svg>
      <span>Enter an Add., City and State or Zip</span>
      <svg width="20" height="20"><circle cx="8" cy="8" r="6.5" fill="none" stroke="#0b55a5" stroke-width="2"/><path d="M13 13l6 6" stroke="#0b55a5" stroke-width="2"/></svg>
    </div>
    <p>We're here to help in case of an emergency, Call Us</p>
    <div class="num">123.456.7890</div>
  </div>
</section>

<footer class="site-footer">
  <div class="f-about">
    <h4><b>TrueLane</b> Collision Repair</h4>
    <p>Fix Right, the first time, every time.<br>TrueLane, The intelligent choice in collision repair.</p>
    <div class="social-label">Get Social:</div>
    <div class="social"><i></i><i class="on"></i><i></i><i></i></div>
    <div class="f-copy">© 2016 TrueLane Collision Repair,<br>All rights reserved.</div>
  </div>
  <div class="f-links">
    <h4>Quick Link</h4>
    <div class="f-cols">
      <ul><li>Home</li><li class="on">Company</li><li>Repair Services</li><li>Our Process</li><li>Careers</li><li>Customer Review</li><li>Feedback</li><li>Location</li><li>Contact</li></ul>
      <ul><li>Legal</li><li>Acquisitions</li><li>Gurantee</li><li>Agent</li><li>Privacy Policy</li><li>Terms of Use</li><li>Sitemap</li><li>FAQ</li></ul>
    </div>
  </div>
  <div class="f-loc">
    <h4>Locations</h4>
    <p>4820 Orchard Lane<br>Westbrook Avenue<br>KY 40100</p>
    <p>Phone:<br>123.456.7890</p>
    <p>Email:<br>support@truelane.example</p>
  </div>
  <svg class="to-top" width="26" height="30" viewBox="0 0 26 30"><path d="M13 2 2 13h7v15h8V13h7z" fill="none" stroke="#888" stroke-width="2"/></svg>
</footer>

</body>
</html>
```